Consulting and solution company website in MS Webmatrix

We need a website for a new healthcare consulting company that provides management consulting and innovative solutions for patient safety. We offer 1 product with plans to add 2 more and we offer consulting services to implement, train, select, improve, the patient safety programs. We provide services to both patient safety organizations and health care provider's (mainly hospitals and health systems). We want the website to convey an innovative, hard-working, energetic company bringing new ideas to healthcare. We do not want a bunch of stock pictures of people looking smart and busy in suits and doctor/nurse garb. T We love adventure, jumping ino the middle of a problem, and are thrilled to be a small and disruptive startup. The problems are very serious and complex issues so we have to tasteful in the design but not typical and boring. he site must be in .net and be device responsive. We will manage the site in MS Webmatrix and if db is used it must be MS SQL. Many of the new and fresh templates I have seen are great. We just can't seem to pull it all together when we start "tweaking" the design. We have modified a standard template to demonstrate where we are headed, but need a higher quality than we are able to build.

My current test site is at http://sandbox.brightquillsolutions.example/

Sites I like
http://www.vormitsoftware.example/
http://ledgerly.zandaro.example/
https://www.taskharbor.example/
http://www.dealmoor.example/
http://www.wbkta.example/

Companies in my market:
www.Mvoyields.example
www.Bramblegrp.example
www.Tksolutions.example
www.Velmarix.example

Target Market(s)

Healthcare providers like chief executives of hospitals, Nursing administrators, Patient Safety Professionals (www.gdkw.example) and physicians/Chief Medical Officers.

Industry/Entity Type

Management Consulting

Font styles to use
Sans Serif

Requirements
Must have
• Must have a put together feel graphically, clean, simple
Must be able to own all design materials.
Must be able to update content with some homework by us
Must have a picture slider
Must be based on .net/mssql.
Nice to have
• Blog page behind a registration process
Register and pull down whitepaper materials
Responsive design

```html
<!DOCTYPE html>
<html lang="en">
<head>
<meta charset="utf-8">
<title>BrightQuill – Patient Safety Consulting</title>
<link href="https://fonts.googleapis.com/css2?family=Mulish:wght@300;400;600;800&display=swap" rel="stylesheet">
<style>
:root{
  --green-dark:#13301a;
  --green-deep:#0d3b16;
  --green-nav:#1e6d24;
  --text:#333;
  --text-soft:#555;
  --muted:#888;
  --band:#efefef;
  --band-light:#e4e4e4;
  --footer:#1c1c1c;
  --white:#fff;
  --sky-top:#dfe9f6;
  --sky-mid:#3b6fd8;
  --sky-deep:#1a3fa8;
}
*{margin:0;padding:0;box-sizing:border-box}
html,body{width:726px;height:1200px;overflow:hidden}
body{font-family:'Mulish',sans-serif;color:var(--text);background:var(--white);position:relative}
.abs{position:absolute}

.topbar{left:0;top:0;width:726px;height:28px;background:#f0f0f0}
.topbar .account{left:490px;top:9px;font-size:7px;color:var(--muted);letter-spacing:.2px}
.topbar .search{left:566px;top:6px;width:128px;height:15px;background:var(--white);border:1px solid #ccc;font-size:7px;color:#aaa;padding:3px 4px}
.topbar .search svg{position:absolute;right:3px;top:2px}

.header{left:0;top:28px;width:726px;height:70px;background:var(--white)}
.logo{left:32px;top:22px;display:flex;align-items:center;gap:6px}
.logo .mark{width:14px;height:14px;background:var(--green-deep)}
.logo .name{font-size:24px;font-weight:600;color:var(--green-deep);letter-spacing:-.3px}
.nav{top:43px;left:0;width:726px;font-size:9.5px;color:#444}
.nav span{position:absolute;white-space:nowrap}
.nav .active{color:var(--green-nav)}

.hero{left:0;top:98px;width:726px;height:294px;background:linear-gradient(170deg,var(--sky-top) 0%,#6b9ae8 22%,var(--sky-mid) 50%,var(--sky-deep) 100%)}
.hero .arrow{position:absolute;top:124px;width:32px;height:32px;border-radius:50%;background:rgba(255,255,255,.85)}
.hero .arrow svg{position:absolute;left:9px;top:8px}
.hero .kicker{right:73px;top:145px;font-size:12px;color:var(--white);text-align:right}
.hero h1{right:73px;top:165px;font-size:23.5px;line-height:27px;font-weight:800;color:var(--white);text-align:right}
.hero .btn{left:554px;top:226px;width:99px;height:28px;background:var(--green-dark);color:var(--white);font-size:9.5px;display:flex;align-items:center;justify-content:center}

.features{left:0;top:392px;width:726px;height:161px;background:var(--band);overflow:hidden}
.features .diag{left:0;top:0}
.feature h2{font-size:16px;font-weight:400;color:#222;position:absolute;white-space:nowrap}
.feature ul{list-style:none;position:absolute;font-size:10.2px;color:#444;line-height:16.5px}
.feature li::before{content:"";display:inline-block;border-left:3px solid #444;border-top:2.5px solid transparent;border-bottom:2.5px solid transparent;margin-right:6px;vertical-align:1px}

.about{left:32px;top:583px;width:330px}
.section-title{font-size:19px;font-weight:300;color:#222}
.about p{margin-top:18px;font-size:10px;line-height:16.4px;color:var(--text-soft)}
.btn-dark{position:absolute;background:var(--green-dark);color:var(--white);font-size:9px;display:flex;align-items:center;justify-content:center}

.help{left:439px;top:583px}
.field{position:absolute;left:2px;width:215px;border:1px solid #bbb;font-size:7px;color:#999;padding:7px 6px;background:var(--white)}

.services{left:0;top:828px;width:726px;height:266px;background:var(--band)}
.services .section-title{position:absolute;top:18px;width:726px;text-align:center}
.service{position:absolute;top:65px;width:150px;margin-left:-75px;text-align:center}
.service .disc{width:60px;height:60px;border-radius:50%;background:var(--green-deep);margin:0 auto;position:relative}
.service .disc svg{position:absolute;left:18px;top:14px}
.service h3{margin-top:14px;font-size:11.5px;font-weight:400;color:#111}
.service p{margin-top:5px;font-size:8.6px;line-height:11.3px;color:var(--text-soft)}
.service .more{margin:7px auto 0;width:55px;height:16px;background:var(--green-deep);color:var(--white);font-size:7px;display:flex;align-items:center;justify-content:center}

.footer{left:0;top:1094px;width:726px;height:106px;background:var(--footer)}
.footer .links{position:absolute;top:30px;width:726px;text-align:center;font-size:7.5px;color:#888;word-spacing:1px}
.footer .links span{margin:0 6px}
.footer .copy{position:absolute;top:49px;width:726px;text-align:center;font-size:6px;color:#444}
.footer .social{position:absolute;top:70px;left:308px;display:flex;gap:3px}
.footer .social span{width:20px;height:20px;border-radius:50%;background:#999}
</style>
</head>
<body>

<div class="abs topbar">
  <div class="abs account">LOGIN | REGISTER</div>
  <div class="abs search">Search
    <svg width="10" height="10" viewBox="0 0 10 10"><circle cx="4" cy="4" r="3" fill="none" stroke="#222" stroke-width="1.4"/><line x1="6.2" y1="6.2" x2="9.3" y2="9.3" stroke="#222" stroke-width="1.6"/></svg>
  </div>
</div>

<header class="abs header">
  <div class="abs logo"><span class="mark"></span><span class="name">BrightQuill</span></div>
  <nav class="abs nav">
    <span class="active" style="left:427px">HOME</span>
    <span style="left:470px">ABOUT US</span>
    <span style="left:532px">SOLUTIONS</span>
    <span style="left:596px">SERVICES</span>
    <span style="left:651px">CONTACT</span>
  </nav>
</header>

<section class="abs hero" role="img" aria-label="Photo of a team of skydivers linking hands in free fall above the clouds">
  <div class="arrow" style="left:15px"><svg width="14" height="16" viewBox="0 0 14 16"><path d="M10 2 L4 8 L10 14" fill="none" stroke="#777" stroke-width="2.6"/></svg></div>
  <div class="arrow" style="left:677px"><svg width="14" height="16" viewBox="0 0 14 16"><path d="M4 2 L10 8 L4 14" fill="none" stroke="#777" stroke-width="2.6"/></svg></div>
  <div class="abs kicker">BE PART OF THE SAFETY SOLUTION</div>
  <h1 class="abs">OPTIMIZE THE BENEFITS<br>OF YOUR PSO</h1>
  <div class="abs btn">MORE INFO</div>
</section>

<section class="abs features">
  <svg class="abs diag" width="726" height="161"><polygon points="425,0 726,0 726,161 268,161" fill="var(--band-light)"/></svg>
  <div class="feature">
    <svg class="abs" style="left:98px;top:46px" width="44" height="44" viewBox="0 0 44 44" fill="none" stroke="var(--green-deep)" stroke-width="2.2">
      <ellipse cx="16" cy="7" rx="13" ry="4.5"/>
      <path d="M3 7v24c0 2.5 6 4.5 13 4.5"/><path d="M29 7v9"/>
      <path d="M3 15c0 2.5 6 4.5 13 4.5s13-2 13-4.5"/>
      <path d="M3 23c0 2.5 6 4.5 13 4.5"/>
      <circle cx="31" cy="30" r="10"/>
      <path d="M26 30h9M32 26l4 4-4 4"/>
    </svg>
    <h2 style="left:157px;top:44px">Send to PSO's</h2>
    <ul style="left:159px;top:70px">
      <li>No more duplicate entry</li>
      <li>Keep your current taxonomy</li>
      <li>Track what you submit</li>
      <li>Join the SafeHub</li>
    </ul>
  </div>
  <div class="feature">
    <svg class="abs" style="left:402px;top:52px" width="40" height="42" viewBox="0 0 40 42" fill="none" stroke="var(--green-deep)" stroke-width="2.4">
      <path d="M14 30c0-5-6-7-6-14a12 12 0 0 1 24 0c0 7-6 9-6 14z"/>
      <path d="M15 34h10M16 38h8"/>
      <path d="M20 0v3M4 16H1M39 16h-3M8 5l2 2M32 5l-2 2"/>
    </svg>
    <h2 style="left:461px;top:44px">Program Optimization</h2>
    <ul style="left:463px;top:70px">
      <li>Hardwire High Reliablity</li>
      <li>Maximize Actionable</li>
      <li>Information</li>
      <li>Close the loop</li>
    </ul>
  </div>
</section>

<section class="abs about">
  <h2 class="section-title" style="padding-left:2px">About Us</h2>
  <p>Lorem ipsum dolor sit amet, consec tetuer adipiscing elit. aesent ves­tibulum molestielacus. Aenean nonummy hendrerit mauris. Phasellus porta. Fusce suscipit varius mi. Lorem ipsum dolor sit amet, consec tetuer adipiscing elit. aesent vestibulum molestielacus. Aenean non­ummy hendrerit mauris. Phasellus porta. Fusce suscipit varius mi. Lorem ipsum dolor sit amet, consec tetuer adipiscing elit. Aenean nonummy hendrerit mauris. Phasellus porta. Fusce suscipit varius mi. Lorem ipsum dolor sit amet, consec tetuer adipiscing elit.</p>
  <div class="btn-dark" style="left:0;top:187px;width:78px;height:26px">READ MORE</div>
</section>

<section class="abs help">
  <h2 class="section-title">How can we help?</h2>
  <div class="field" style="top:47px;height:21px;padding-top:6px">YOUR NAME</div>
  <div class="field" style="top:79px;height:21px;padding-top:6px">YOUR EMAIL</div>
  <div class="field" style="top:111px;height:66px">QUESTIONS / COMMENTS</div>
  <div class="btn-dark" style="left:3px;top:187px;width:64px;height:26px">SUBMIT</div>
</section>

<section class="abs services">
  <h2 class="section-title">Our Services</h2>
  <div class="service" style="left:109px">
    <div class="disc"><svg width="24" height="31" viewBox="0 0 24 31" fill="none" stroke="#fff" stroke-width="1.6"><rect x="1" y="3" width="22" height="27"/><path d="M5 1v4M9.5 1v4M14 1v4M18.5 1v4"/><path d="M5 11l1.5 1.5 2-2.5M11 11.5h8M5 17l1.5 1.5 2-2.5M11 17.5h8M5 23l1.5 1.5 2-2.5M11 23.5h8"/></svg></div>
    <h3>Needs Assessment</h3>
    <p>Our proprietary methodology evaluates your current program systematically comparing to indus­try standards and national</p>
    <div class="more">MORE +</div>
  </div>
  <div class="service" style="left:282px">
    <div class="disc"><svg width="24" height="31" viewBox="0 0 24 31" fill="none" stroke="#fff" stroke-width="1.6"><rect x="1" y="3" width="22" height="27"/><path d="M5 1v4M9.5 1v4M14 1v4M18.5 1v4"/><path d="M5 11l1.5 1.5 2-2.5M11 11.5h8M5 17l1.5 1.5 2-2.5M11 17.5h8M5 23l1.5 1.5 2-2.5M11 23.5h8"/></svg></div>
    <h3>Process Analysis</h3>
    <p>Our proprietary methodology evaluates your current program systematically comparing to indus­try standards and national</p>
    <div class="more">MORE +</div>
  </div>
  <div class="service" style="left:452px">
    <div class="disc"><svg width="24" height="31" viewBox="0 0 24 31" fill="none" stroke="#fff" stroke-width="1.6"><rect x="1" y="3" width="22" height="27"/><path d="M5 1v4M9.5 1v4M14 1v4M18.5 1v4"/><path d="M5 11l1.5 1.5 2-2.5M11 11.5h8M5 17l1.5 1.5 2-2.5M11 17.5h8M5 23l1.5 1.5 2-2.5M11 23.5h8"/></svg></div>
    <h3>Optimization</h3>
    <p>Our proprietary methodology evaluates your current program systematically comparing to indus­try standards and national</p>
    <div class="more">MORE +</div>
  </div>
  <div class="service" style="left:618px">
    <div class="disc"><svg width="24" height="31" viewBox="0 0 24 31" fill="none" stroke="#fff" stroke-width="1.6"><rect x="1" y="3" width="22" height="27"/><path d="M5 1v4M9.5 1v4M14 1v4M18.5 1v4"/><path d="M5 11l1.5 1.5 2-2.5M11 11.5h8M5 17l1.5 1.5 2-2.5M11 17.5h8M5 23l1.5 1.5 2-2.5M11 23.5h8"/></svg></div>
    <h3>Implementation</h3>
    <p>Our proprietary methodology evaluates your current program systematically comparing to indus­try standards and national</p>
    <div class="more">MORE +</div>
  </div>
</section>

<footer class="abs footer">
  <div class="links"><span>HOME</span><span>ABOUT US</span><span>SOLUTIONS</span><span>SERVICES</span><span>CONTACT</span></div>
  <div class="copy">ALL RIGHTS RESERVED. COPYRIGHTS © 2014</div>
  <div class="social" aria-label="Social links"><span></span><span></span><span></span><span></span><span></span></div>
</footer>

</body>
</html>
```